Flyer Design Project

Our company focuses on selling Consumer products like home furniture, home decor, electronics and accessories by public auction. We need a flyer design that will showcase these products with pictures and text. Illustration and desciption on the flyer is always genetic and never changes, The flyer design should be simple and straight forward with limited graphic design and instead focus on product description and emphasise on words Public Auction, and the word AUCTION being the main heading on the flyer. Multilpe colours are prefered.

Target Market(s)

Age group between 30-65 lmajority living in rural, homeowners and looking for a great quality product at an economical price

Industry/Entity Type

Graphic Design

Requirements
Must have
• The flyer should be tri-fold 11x17 inches in size fron and back.
Nice to have
• To show consumers that they have an opportunity to save money by attending our auctions.
Should not have
• The flyer design should not look too corporate or sophisticated. Simple approach to target consumers since most of them live in rural areas.

```html
<!DOCTYPE html>
<html lang="en">
<head>
<meta charset="utf-8">
<title>Public Auction Flyer</title>
<link rel="stylesheet" href="https://fonts.googleapis.com/css2?family=League+Gothic&family=Patrick+Hand&family=Patrick+Hand+SC&family=Bowlby+One+SC&family=Quicksand:wght@500;700&display=swap">
<style>
  :root {
    --bg: #e9e6e1;
    --yellow: #f6c52e;
    --yellow-deep: #f0ad2f;
    --pink: #ef4d69;
    --pink-dark: #b8233f;
    --orange: #f47f58;
    --orange-light: #f5a23d;
    --black: #151213;
    --white: #ffffff;
  }
  * { margin: 0; padding: 0; box-sizing: border-box; }
  html, body { width: 1200px; height: 1003px; overflow: hidden; background: var(--bg); }
  .canvas { position: relative; width: 1200px; height: 1003px; }

  .panel {
    position: absolute; top: 52px; width: 460px; height: 900px; overflow: hidden;
    box-shadow: 0 6px 18px rgba(0,0,0,.18);
  }

  /* Back panel */
  .panel--back {
    left: 120px;
    background: linear-gradient(160deg, var(--orange) 0%, #f48b4f 55%, var(--orange-light) 100%);
    color: var(--white); text-align: center;
  }
  .corner { position: absolute; }
  .corner--top { top: 0; left: 0; width: 460px; height: 60px; }
  .corner--bottom { bottom: 0; left: 0; width: 460px; height: 70px; }
  .event-day {
    position: absolute; top: 70px; left: 0; right: 0;
    font-family: "Bowlby One SC", sans-serif; font-size: 58px; letter-spacing: 1px; line-height: 1;
  }
  .event-date {
    position: absolute; top: 138px; left: 0; right: 0;
    font-family: "Patrick Hand SC", cursive; font-size: 34px; letter-spacing: 2px;
  }
  .event-date b { font-family: "Bowlby One SC", sans-serif; font-weight: 400; font-size: 32px; }
  .event-phone {
    position: absolute; top: 186px; left: 0; right: 0;
    font-family: "Bowlby One SC", sans-serif; font-size: 42px; letter-spacing: 1px;
  }
  .location-map {
    position: absolute; top: 265px; left: 60px; width: 340px; height: 210px;
    background: var(--black); border-radius: 36px;
  }
  .location-map::after {
    content: ""; position: absolute; inset: 30px 40px; border-radius: 8px;
    background: linear-gradient(135deg, #3a2f1c, #5b4a1c);
  }
  .venue {
    position: absolute; top: 510px; left: 0; right: 0;
    font-family: "Patrick Hand SC", cursive; font-size: 25px; letter-spacing: 2px; line-height: 1.25;
  }
  .company-name {
    position: absolute; top: 650px; left: 0; right: 0;
    font-family: "Patrick Hand SC", cursive; font-size: 34px; letter-spacing: 2px;
    display: flex; justify-content: center; align-items: center; gap: 12px;
  }
  .company-name .dot { width: 16px; height: 16px; border-radius: 50%; background: var(--white); }
  .company-email {
    position: absolute; top: 705px; left: 0; right: 0;
    font-family: "Quicksand", sans-serif; font-weight: 700; font-size: 24px;
  }
  .payment-cards {
    position: absolute; top: 752px; left: 0; right: 0;
    display: flex; justify-content: center; gap: 22px;
  }
  .payment-card { width: 86px; height: 50px; border-radius: 7px; background: var(--white); opacity: .92; }

  /* Front cover */
  .panel--front {
    left: 620px;
    background: linear-gradient(180deg, var(--yellow) 0%, var(--yellow-deep) 100%);
    text-align: center;
  }
  .front-corner { position: absolute; top: 0; right: 0; width: 460px; height: 70px; }
  .headline {
    position: absolute; top: 72px; left: 10px; right: 10px;
    font-family: "Patrick Hand SC", cursive; font-weight: 400; font-size: 34px; line-height: 1.05;
    color: var(--black); letter-spacing: 0.5px; white-space: nowrap;
  }
  .title {
    position: absolute; left: 0; right: 0;
    font-family: "League Gothic", sans-serif; color: var(--pink);
    text-shadow: 3px 3px 0 var(--pink-dark), 6px 6px 0 rgba(140,20,45,.55);
    line-height: 1; letter-spacing: 2px;
  }
  .title--public { top: 240px; font-size: 146px; }
  .title--auction { top: 370px; font-size: 164px; }
  .tagline {
    position: absolute; top: 572px; left: 118px; width: 224px; height: 128px;
    background: var(--black); border-radius: 28px;
    display: flex; align-items: center; justify-content: center;
    font-family: "Patrick Hand", cursive; font-size: 29px; line-height: 1.05; color: var(--white);
  }
  .floor-band {
    position: absolute; left: 0; right: 0; bottom: 0; height: 120px; background: var(--pink);
  }
  .furniture-art {
    position: absolute; left: 30px; right: 30px; top: 720px; height: 165px;
    background: linear-gradient(180deg, rgba(21,18,19,.85), rgba(21,18,19,.7));
    border-radius: 10px;
  }
</style>
</head>
<body>
<main class="canvas">

  <section class="panel panel--back" aria-label="Back panel">
    <svg class="corner corner--top" viewBox="0 0 460 60" preserveAspectRatio="none">
      <polygon points="0,0 460,0 0,28" fill="#f6c52e"/>
    </svg>
    <p class="event-day">SATURDAY</p>
    <p class="event-date">SEPTEMBER <b>17</b> AT <b>1</b></p>
    <p class="event-phone">555.010.2468</p>
    <div class="location-map" role="img" aria-label="Street map showing the route to the venue"></div>
    <p class="venue">MAPLE GROVE COMMUNITY CENTRE<br>1200 CEDAR STREET, MAPLE GROVE<br>PREVIEW : 12 NOON</p>
    <p class="company-name"><span class="dot"></span>BRIGHTLOT</p>
    <p class="company-email">info@brightlot.com</p>
    <div class="payment-cards">
      <span class="payment-card"></span>
      <span class="payment-card"></span>
    </div>
    <svg class="corner corner--bottom" viewBox="0 0 460 70" preserveAspectRatio="none">
      <polygon points="0,70 460,70 460,10" fill="#ef4d69"/>
      <polygon points="300,70 460,70 460,40" fill="#f6c52e"/>
    </svg>
  </section>

  <section class="panel panel--front" aria-label="Front cover">
    <svg class="front-corner" viewBox="0 0 460 70" preserveAspectRatio="none">
      <polygon points="0,0 460,0 460,34" fill="#ef4d69"/>
    </svg>
    <h2 class="headline">MASSIVE INVENTORY<br>CLEAROUT OF NEW FINE<br>FURNITURE, HOMEDECOR,<br>ELECTRONICS &amp; ACCESORIES</h2>
    <h1>
      <span class="title title--public">PUBLIC</span>
      <span class="title title--auction">AUCTION</span>
    </h1>
    <p class="tagline">You Can't<br>Afford To Miss<br>This Event!</p>
    <div class="floor-band"></div>
    <div class="furniture-art" role="img" aria-label="Silhouettes of an urn on a side table, an armchair and a dining chair"></div>
  </section>

</main>
</body>
</html>
```